Health & Fitness Author & Public Speaker Needs Visually Stunning Web Design!

We've FINALLY got around to launching a website for Marisol Kettering - Australian Food Coach and Health & Fitness Expert. The website is to promote her new healthy eating program - "Bright Plate Living".
For a compehensive outline of exactly what we are after, please see the following attached files:
(1) Web Layout (wireframe, content/copy, links to photos to use, sample page we love)
(2) Style Guide (these are the colours, and overall feel we want)
Photos that we'd like used (of Marisol, and food/meals) can be found at these URL's:
Profile: https://www.filecrate.net/sh/q4r8vzkp2w7ttc3/H5M2xpLbeq
PixVault: https://www.filecrate.net/sh/b7mfwqjd3ue58an/9pq4Rtyhh2
HINT:
Before you do ANYTHING - check out this site as it is pretty much EXACTLY what we're after, but with our branding/colours/style: http://tovahlund.net/
As we will need to revamp our existing Chatterbook page & other printed material, there may be the potential for further work for the successful designer in the future.
Thanks & Good Luck!
Dorian Welch
Marketing & Business Development Manager
Bright Plate Living
Target Market(s)
Women, Ages 24 - 45, Interested in Healthly Eating & Fitness
Industry/Entity Type
Business
Look and feel
Each slider illustrates characteristics of the customer's brand and the style your logo design should communicate.

```html
<!DOCTYPE html>
<html lang="en">
<head>
<meta charset="utf-8">
<title>Bright Plate Living with Marisol Kettering</title>
<link href="https://fonts.googleapis.com/css2?family=Federo&family=Josefin+Sans:wght@300;400&family=Oswald:wght@400;500&family=Ubuntu:wght@400;500;700&family=Yanone+Kaffeesatz:wght@300;400&display=swap" rel="stylesheet">
<style>
  :root {
    --page-dark: #2b2828;
    --ink: #1c1c1c;
    --body-ink: #3a3a3a;
    --pink: #e8184f;
    --pink-soft: #f7a3bb;
    --maroon: #9e0b34;
    --purple: #7d1a86;
    --rule: #c9c9c9;
    --green: #6ba51b;
    --green-dark: #3f6b10;
    --orange: #f7941d;
    --footer-ink: #a9a7a7;
  }
  * { box-sizing: border-box; margin: 0; padding: 0; }
  html, body { width: 926px; height: 1200px; overflow: hidden; }
  body { background: var(--page-dark); font-family: "Ubuntu", sans-serif; color: var(--ink); position: relative; }

  .site { position: absolute; left: 29px; top: 0; width: 868px; height: 1140px; background: #fff; }

  /* header */
  .site-header { position: absolute; left: 0; top: 0; width: 868px; height: 56px; background: linear-gradient(90deg, #f3f2f0, #e9e8e5 50%, #f1f0ee); }
  .logo { position: absolute; left: 68px; top: 18px; font: 500 15px "Ubuntu", sans-serif; color: var(--pink); }
  .main-nav { position: absolute; top: 20px; left: 0; width: 868px; font: 700 13px "Ubuntu", sans-serif; color: #2c2c2c; }
  .main-nav span { position: absolute; white-space: nowrap; }

  /* hero */
  .hero { position: absolute; left: 0; top: 56px; width: 868px; height: 387px; overflow: hidden; }
  .hero-photo { position: absolute; inset: 0; background: radial-gradient(ellipse at 28% 55%, #e4dfd8 0%, #b9b2a8 45%, #8d867c 100%); }
  .tag { position: absolute; left: 432px; height: 31px; background: rgba(255,255,255,0.9); font: 400 24px "Federo", sans-serif; color: var(--purple); padding: 3px 0 0 10px; letter-spacing: 1px; white-space: nowrap; }
  .tag-with { position: absolute; left: 590px; top: 142px; width: 46px; height: 46px; border-radius: 50%; background: var(--pink); color: #fff; font: 400 15px "Federo", sans-serif; text-align: center; line-height: 46px; }
  .hero-title { position: absolute; left: 420px; width: 400px; top: 190px; text-align: center; font: 300 34px "Josefin Sans", sans-serif; color: var(--pink); white-space: nowrap; }
  .hero-with { position: absolute; left: 430px; width: 380px; top: 238px; height: 14px; }
  .hero-with::before, .hero-with::after { content: ""; position: absolute; top: 7px; width: 127px; height: 1px; background: #555; }
  .hero-with::before { left: 0; } .hero-with::after { right: 0; }
  .hero-with span { position: absolute; left: 0; right: 0; text-align: center; font: 400 13px "Josefin Sans", sans-serif; color: #333; letter-spacing: 2px; }
  .hero-name { position: absolute; left: 400px; width: 440px; top: 258px; text-align: center; font: 400 34px "Federo", sans-serif; color: var(--purple); white-space: nowrap; }
  .hero-rule { position: absolute; left: 430px; width: 380px; top: 311px; height: 1px; background: #555; }

  /* signup band */
  .signup-band { position: absolute; left: 0; top: 443px; width: 868px; height: 74px; background: var(--pink); }
  .band-title { position: absolute; left: 74px; top: 15px; font: 700 14px "Ubuntu", sans-serif; color: #fff; white-space: nowrap; }
  .band-sub { position: absolute; left: 74px; top: 37px; font: 700 9.5px/13px "Ubuntu", sans-serif; color: var(--pink-soft); text-transform: uppercase; white-space: nowrap; }
  .field { position: absolute; background: #fff; border: 1px solid #bbb; font: 400 9px "Ubuntu", sans-serif; color: #555; padding: 0 7px; display: flex; align-items: center; }
  .btn { position: absolute; display: flex; align-items: center; justify-content: center; font: 700 9px "Ubuntu", sans-serif; color: #fff; background: var(--maroon); border-radius: 2px; }

  /* posts */
  .post-title { position: absolute; left: 74px; width: 440px; font: 700 20px/24px "Ubuntu", sans-serif; color: var(--ink); }
  .post-body { position: absolute; left: 75px; width: 427px; font: 400 9.8px/13px "Ubuntu", sans-serif; color: var(--body-ink); text-align: justify; }
  .post-meta { position: absolute; left: 75px; font: 400 8px "Ubuntu", sans-serif; color: #333; display: flex; align-items: center; gap: 4px; }
  .share-dot { width: 18px; height: 18px; background: #5c5c5c; border-radius: 2px; margin-left: 4px; }
  .share-dot + .share-dot { margin-left: 0; }
  .share-dot.light { background: #a8a8a8; }
  .post-rule { position: absolute; left: 74px; width: 422px; height: 1px; background: var(--rule); }

  /* sidebar */
  .promo { position: absolute; left: 530px; width: 255px; }
  .guide { top: 547px; height: 213px; background: linear-gradient(180deg, #dcdcdc 0%, #f4f4f4 40%, #fff 55%); }
  .guide-photo { position: absolute; left: 0; right: 0; bottom: 0; height: 140px; background: linear-gradient(120deg, #d9c7a2 0%, #8fb24a 45%, #c9412b 70%, #5f8f2c 100%); }
  .guide-line1 { position: absolute; left: 23px; top: 20px; font: 300 29px "Yanone Kaffeesatz", sans-serif; color: #555; white-space: nowrap; }
  .guide-line2 { position: absolute; left: 23px; top: 47px; font: 300 26px "Yanone Kaffeesatz", sans-serif; color: var(--pink); white-space: nowrap; }
  .guide-btn { position: absolute; left: 23px; top: 80px; width: 96px; height: 29px; background: var(--green); color: #fff; font: 700 12.5px "Ubuntu", sans-serif; display: flex; align-items: center; justify-content: center; z-index: 1; }

  .challenge { top: 789px; height: 173px; }
  .challenge-photo { position: absolute; inset: 0; background: linear-gradient(110deg, #f0a33c 0%, #a7c76a 30%, #c9ccc9 55%, #eef0ec 100%); }
  .challenge-title { position: absolute; left: 90px; top: 11px; font: 500 26px "Oswald", sans-serif; color: var(--pink); white-space: nowrap; letter-spacing: -0.5px; transform: scaleX(0.8); transform-origin: left; }
  .challenge-panel { position: absolute; left: 92px; top: 42px; width: 171px; height: 100px; background: linear-gradient(135deg, #2f6b12, #5f9b23 60%, #3b7416); }
  .challenge-panel p { position: absolute; left: 13px; top: 12px; font: 300 15px/16px "Yanone Kaffeesatz", sans-serif; color: #fff; white-space: nowrap; }
  .challenge-panel p strong { font-weight: 300; font-size: 19px; }
  .challenge-btn { position: absolute; left: 25px; top: 54px; width: 103px; height: 29px; background: var(--orange); color: #fff; font: 700 12.5px "Ubuntu", sans-serif; display: flex; align-items: center; justify-content: center; }

  .join-title { position: absolute; left: 559px; width: 256px; top: 984px; text-align: center; font: 400 17px "Yanone Kaffeesatz", sans-serif; color: var(--green-dark); }
  .join-copy { position: absolute; left: 559px; width: 256px; top: 1011px; text-align: center; font: 400 9.5px/14px "Ubuntu", sans-serif; color: #333; }
  .join-copy .accent { color: var(--pink); }

  /* footer */
  .site-footer { position: absolute; left: 29px; top: 1140px; width: 868px; height: 60px; }
  .footer-nav { position: absolute; left: 0; top: 10px; font: 700 13px "Ubuntu", sans-serif; color: var(--footer-ink); }
  .footer-nav .sep { color: var(--pink); margin: 0 5px; }
  .copyright { position: absolute; left: 0; top: 31px; font: 500 8px "Ubuntu", sans-serif; color: var(--footer-ink); }
  .social { position: absolute; top: 13px; width: 23px; height: 23px; border-radius: 50%; background: #c4c2c2; }
</style>
</head>
<body>
  <div class="site">
    <header class="site-header">
      <div class="logo">Bright Plate Living</div>
      <nav class="main-nav">
        <span style="left:496px">HOME</span>
        <span style="left:572px">ABOUT</span>
        <span style="left:651px">THE PLAN</span>
        <span style="left:750px">SHOP</span>
      </nav>
    </header>

    <section class="hero">
      <div class="hero-photo" role="img" aria-label="Photo of Marisol Kettering smiling against a weathered stone wall, holding a bunch of green grapes"></div>
      <div class="tag" style="top:81px;width:131px">GET SLIM</div>
      <div class="tag" style="top:112px;width:222px">BOOST ENERGY</div>
      <div class="tag" style="top:145px;width:152px">GUILT FREE</div>
      <div class="tag-with">with</div>
      <div class="hero-title">BRIGHT PLATE LIVING!</div>
      <div class="hero-with"><span>WITH</span></div>
      <div class="hero-name">MARISOL KETTERING</div>
      <div class="hero-rule"></div>
    </section>

    <section class="signup-band">
      <div class="band-title">Join the BRIGHT PLATE LIVING MOVEMENT!</div>
      <div class="band-sub">Get a weekly serving of inspiration &amp; advice that<br>will change your life...bring it on!</div>
      <div class="field" style="left:401px;top:24px;width:129px;height:24px">Your Name</div>
      <div class="field" style="left:539px;top:24px;width:129px;height:24px">Your Email</div>
      <div class="btn" style="left:673px;top:23px;width:111px;height:25px">HOOK ME UP</div>
    </section>

    <article>
      <h2 class="post-title" style="top:543px">Integer placerat, tellus et blandit molestie, purus leo semper massa, scelerisque</h2>
      <p class="post-body" style="top:597px">Lorem ipsum dolor sit amet, consectetur adipiscing elit. Donec at tortor eget lorem porta aliquam. Praesent eget dolor quam, sit amet porttitor tortor. Curabitur ut nisi felis. Donec sed justo neque. Integer placerat, tellus et blandit molestie, purus leo semper massa, scelerisque dictum purus enim nec est. Aenean in mi tortor. Fusce sed mi urna. Phasellus vitae risus id erat fermentum suscipit. Aliquam mattis, odio vel adipiscing tincidunt, orci augue tincidunt turpis, at dapibus quam elit vitae turpis. Maecenas egestas nibh est. Phasellus suscipit tincidunt ligula, sit amet tristique turpis lacinia vel tellus et blandit molestie, purus leo semper massa, scelerisque dictum purus enim nec est.</p>
      <div class="post-meta" style="top:714px">11th January 2012 | Share <span class="share-dot"></span><span class="share-dot"></span><span class="share-dot light"></span></div>
      <div class="post-rule" style="top:751px"></div>
    </article>

    <article>
      <h2 class="post-title" style="top:767px">In hac habitasse platea dictumst. Duis a consequat nisl viverra facilis</h2>
      <p class="post-body" style="top:822px">Nullam eleifend risus vitae massa tincidunt eu feugiat diam vestibulum. Cum sociis natoque penatibus et magnis dis parturient montes, nascetur ridiculus mus. Donec fringilla suscipit diam vel tempus. Cum sociis natoque penatibus et magnis dis parturient montes, nascetur ridiculus mus. Phasellus pellentesque scelerisque ante, nec pulvinar eros euismod eget. Nunc in ullamcorper nunc. Nulla euismod, nisl hendrerit convallis blandit, diam turpis lobortis nunc, vitae ultricies turpis lacus vel magna. Class aptent taciti sociosqu ad litora torquent per conubia nostra, per inceptos himenaeos. In hac habitasse platea dictumst. Sed placerat magna non enim blandit ac fermentum mauris elementum. Vivamus malesuada est a justo posuere lobortis. Nullam vel gravida mi. Etiam pellentesque, ligula nec iaculis bibendum, nunc neque euismod nulla, a molestie enim velit a libero.</p>
      <p class="post-body" style="top:968px">Phasellus viverra lorem vel magna eleifend venenatis. Integer convallis sapien at lorem ullamcorper sed viverra massa tempus. Quisque interdum magna vitae ipsum cursus porta. Nam eget pellentesque dolor. Pellentesque habitant morbi tristique senectus et netus et malesuada fames ac turpis egestas. Nullam eleifend risus vitae massa tincidunt eu feugiat diam vestibulum. Cum sociis natoque penatibus et magnis dis parturient montes, nascetur ridiculus mus.</p>
      <div class="post-meta" style="top:1046px">11th January 2012 | Share <span class="share-dot"></span><span class="share-dot"></span><span class="share-dot light"></span></div>
      <div class="post-rule" style="top:1077px"></div>
    </article>

    <aside>
      <div class="promo guide">
        <div class="guide-photo" role="img" aria-label="Photo of a chicken salad wrap with tomatoes and mixed leaves"></div>
        <div class="guide-line1">The ULTIMATE</div>
        <div class="guide-line2">Bright Plate Living Guide</div>
        <div class="guide-btn">GET IT NOW!</div>
      </div>

      <div class="promo challenge">
        <div class="challenge-photo" role="img" aria-label="Photo of fresh oranges, carrots and greens in a metal colander"></div>
        <div class="challenge-title">12 WEEK CHALLENGE</div>
        <div class="challenge-panel">
          <p>HEALTHY, HAPPY &amp; HOT<br><strong>IN NO TIME FLAT!</strong></p>
          <div class="challenge-btn">JOIN US NOW</div>
        </div>
      </div>

      <h3 class="join-title">JOIN THE MOVEMENT!</h3>
      <p class="join-copy">Join the Bright Plate Living Movement and get a free<br>copy of <span class="accent">The Fresh Start Kit</span> (valued $19.00)!</p>
      <div class="field" style="left:559px;top:1052px;width:123px;height:24px">Your Name</div>
      <div class="field" style="left:692px;top:1052px;width:123px;height:24px">Your Email</div>
      <div class="btn" style="left:559px;top:1089px;width:256px;height:24px">HOOK ME UP</div>
    </aside>
  </div>

  <footer class="site-footer">
    <nav class="footer-nav">HOME<span class="sep">/</span>ABOUT<span class="sep">/</span>THE PLAN<span class="sep">/</span>SHOP</nav>
    <div class="copyright">COPYRIGHT © 2013 BRIGHT PLATE LIVING. ALL RIGHTS RESERVED. DISCLAIMER / PRIVACY POLICY</div>
    <span class="social" style="left:772px"></span>
    <span class="social" style="left:808px"></span>
    <span class="social" style="left:843px"></span>
  </footer>
</body>
</html>
```